The Resort at Falconer's Ridge Combo Ticket Package.Stay 3 nights & get 2 Sets of Combo T

Tickets on us email. The Resort at Falconer's Ridge needs an email designed that will reach 1 million email subscribers. It will be our package that when guest stay 3 or more nights they get 2 sets of combo tickets 2 bramwell & tuck and quarry hollow jamboree..
Stay 3 or more nights from now till 8/4/2018 and get 2 Sets of Combo Tickets! So that's 2 tickets to Bramwell & Tuck Supper Show and 2 Tickets to Quarry Hollow Jamboree. The resort website is -> http://falconersridge-example.net/index.php Bramwell& Tuck is -> http://bramwelltucksupperfray-example.com/ and Quarry Hollow Jamboree is http://quarryhollowjam-example.com/ *additional tickets can be purchased at a discounted rate for guest of The Resort only.
They will book on line by clicking the email or calling 800-316-2289
Stay dates are now through 8/4 Must Reserve by 6/15/2018 -> Reserve now this special will be gone in a Flash!
This is a huge savings!

Target Market(s)

This will be sent via email to 1,000,000 email data base that we want to convince its a great deal to reserve 3 nights with us and get the 2 sets of combo tickets absolutely free.

Colors

Designer to choose colors to be used in the design.

Requirements
Must have
• The Resort, Bramwell & Tuck and Quarry Hollow Jamboree logos and images. Will have to visit website to get
• Be consistent with all brands.. I have attached a banner so you can see brand..
• Also may have to atake all images from websites.
Nice to have
• bright and enticing- make the guest want to reserve the deal
Should not have
• Pricing.

```html
<!DOCTYPE html>
<html lang="en">
<head>
<meta charset="utf-8">
<title>The Resort at Falconer's Ridge – Combo Ticket Package</title>
<link rel="stylesheet" href="https://fonts.googleapis.com/css2?family=Playfair+Display:wght@400&family=Open+Sans:wght@400&family=Catamaran:wght@400;600&family=Marck+Script&family=Montserrat:wght@400&display=swap">
<style>
  :root {
    --white: #ffffff;
    --ink: #1a1a1a;
    --muted: #555555;
    --rust: #b5651d;
    --maroon: #8c1c1c;
    --tan: #d39a5b;
    --forest: #1f2b24;
    --gold: #fccb38;
    --badge: #f7c62f;
    --badge-text: #b5651d;
    --red: #a5161d;
    --sky: #e3ebf5;
    --blue: #1f4aa8;
  }
  * { box-sizing: border-box; margin: 0; padding: 0; }
  html, body { width: 1200px; height: 3255px; overflow: hidden; background: var(--white); }
  body { font-family: "Open Sans", sans-serif; color: var(--ink); }

  .hero {
    position: relative; height: 937px;
    background: linear-gradient(180deg, #1d2a8a 0%, #3a4fb0 28%, #6e7fb8 42%, #c98a3c 62%, #4a5a6a 80%, #2b3a3f 100%);
  }
  .brand {
    position: absolute; top: 34px; left: 30px;
    display: flex; align-items: center; gap: 14px;
    font-family: "Playfair Display", serif; font-size: 34px; color: var(--white);
  }
  .brand-dot { width: 40px; height: 40px; border-radius: 50%; background: var(--rust); }
  .toll-free {
    position: absolute; top: 44px; right: 36px;
    font-family: "Catamaran", sans-serif; font-weight: 600; font-size: 35px; color: var(--white);
  }

  .intro { height: 289px; text-align: center; padding-top: 45px; }
  .intro h1 {
    font-family: "Playfair Display", serif; font-weight: 400;
    font-size: 54px; color: var(--rust); line-height: 1.1;
  }
  .intro p {
    width: 1020px; margin: 30px auto 0; font-size: 23px; line-height: 1.62; color: var(--muted);
  }

  .offers-title {
    height: 80px; text-align: center;
    font-family: "Marck Script", cursive; font-size: 56px; color: var(--maroon); line-height: 80px;
  }

  .offer { position: relative; display: flex; height: 506px; }
  .offer + .offer { margin-top: 18px; }
  .offer-copy {
    display: flex; flex-direction: column; justify-content: center; align-items: center;
    text-align: center; font-family: "Catamaran", sans-serif;
  }
  .offer-copy p { font-size: 36px; line-height: 1.42; }
  .offer-copy .site-label { font-weight: 600; font-size: 25px; margin-top: 34px; line-height: 1.5; }
  .offer-copy .site { font-weight: 600; font-size: 25px; line-height: 1.5; }
  .offer--room .offer-copy { width: 538px; background: var(--tan); color: #2a1c10; padding: 0 96px 0 40px; }
  .offer--room .offer-copy p { max-width: 400px; }
  .offer--room .offer-photo { flex: 1; background: linear-gradient(135deg, #b07a45 0%, #d9b27c 40%, #8c5a34 75%, #5a3a22 100%); }
  .offer--spa .offer-photo { width: 542px; background: linear-gradient(135deg, #6b5b52 0%, #c9a89a 45%, #d8dde3 70%, #9fb2c4 100%); }
  .offer--spa .offer-copy { flex: 1; background: var(--forest); color: var(--badge); padding: 0 44px 0 90px; }

  .badge {
    position: absolute; width: 180px; height: 180px; border-radius: 50%;
    background: var(--badge); color: var(--badge-text);
    display: flex; align-items: center; justify-content: center; text-align: center;
    font-family: "Catamaran", sans-serif; font-size: 32px; line-height: 1.2;
  }
  .offer--room .badge { left: 448px; top: 34px; }
  .offer--spa .badge { left: 462px; top: 306px; }

  .fine-print {
    margin-top: 11px; height: 252px; background: var(--gold);
    display: flex; align-items: center; justify-content: center; text-align: center;
    font-family: "Playfair Display", serif; font-size: 51px; line-height: 1.4; color: #5a1a10;
    padding: 0 60px;
  }

  .booking { height: 226px; text-align: center; padding-top: 36px; font-family: "Playfair Display", serif; }
  .booking p { font-size: 44px; line-height: 1.6; color: var(--ink); }
  .booking .phone { color: var(--red); }

  .deadline {
    height: 239px; background: var(--sky);
    display: flex; flex-direction: column; justify-content: center; align-items: center;
    font-family: "Playfair Display", serif; font-size: 36px; line-height: 1.5; color: var(--blue);
  }

  .social { height: 190px; text-align: center; padding-top: 44px; }
  .social p { font-family: "Montserrat", sans-serif; font-size: 26px; color: #333; }
  .social ul { list-style: none; display: flex; justify-content: center; gap: 14px; margin-top: 24px; }
  .social li { width: 48px; height: 48px; border-radius: 50%; background: #111; }
</style>
</head>
<body>
  <header class="hero" role="img" aria-label="Evening photo of the resort building beside its outdoor water park with pools and slides">
    <div class="brand"><span class="brand-dot"></span>The Resort</div>
    <div class="toll-free">TOLL FREE &nbsp;: 800-316-2250</div>
  </header>

  <section class="intro">
    <h1>The Resort at Falconer's Ridge..</h1>
    <p>Visitors to the Misty Ridge Mountains have found The Resort at Falconer's Ridge to be the ideal choice for vacation condo lodging with unsurpassed guest amenities and convenience. Within minutes of Cedar Bend and Ashby Falls, The Resort is located in Millbrook's Falconer's</p>
  </section>

  <h2 class="offers-title">Our Offers</h2>

  <section class="offer offer--room">
    <div class="offer-copy">
      <p>Guest stay 3 or more nights they get 2 sets of combo tickets 2 bramwell &amp; tuck and quarry hollow jamboree..</p>
      <span class="site-label">Our Website :</span>
      <span class="site">bramwelltucksupperfray-example.com</span>
    </div>
    <div class="offer-photo" role="img" aria-label="Photo of a condo living room with sofa chairs, lamp and dining table"></div>
    <div class="badge">Commbo<br>Offer</div>
  </section>

  <section class="offer offer--spa">
    <div class="offer-photo" role="img" aria-label="Photo of guests relaxing in an indoor hot tub"></div>
    <div class="offer-copy">
      <p>Guest stay 3 or more nights they get 2 sets of combo tickets 2 bramwell &amp; tuck and quarry hollow jamboree..</p>
      <span class="site-label">Our Website :</span>
      <span class="site">bramwelltucksupperfray-example.com</span>
    </div>
    <div class="badge">Commbo<br>Offer</div>
  </section>

  <section class="fine-print">*additional tickets can be purchased at a discounted rate for guest of The Resort only.</section>

  <section class="booking">
    <p>They will book on line by clicking the email or</p>
    <p class="phone">Calling 800-316-2289</p>
  </section>

  <section class="deadline">
    <span>Stay dates are now through 8/4 Must Reserve by 6/15/2018</span>
    <span>-Reserve now this special will be gone in a Flash!</span>
    <span>This is a huge savings!</span>
  </section>

  <footer class="social">
    <p>Connet with Us</p>
    <ul aria-label="Social links">
      <li></li><li></li><li></li><li></li>
    </ul>
  </footer>
</body>
</html>
```